Cosmetics Brand Logo and Bottle Label Design

We are creating a new cosmetics brand called "Nolan Whitby" and would like you to create an amazing logo and bottle label for this brand's new 100% pure argan oil product.
For the logo, we really like the logo's of Marin Calloway and Vessa. The text should be Sans Serif (without feet).
For the actual bottle label, please find attached labels of one of our competitors design which really like. We really like the simplicity and elegance of the design. The only difference is that our product will be using light turqoise as the brand color. Please feel free to add your own creativity into it as well.
Industry/Entity Type
Cosmetics
Logo Text
Nolan Whitby
Font styles to use

```html
<!DOCTYPE html>
<html lang="en">
<head>
<meta charset="utf-8">
<title>Nolan Whitby – Argan Oil Packaging</title>
<link rel="stylesheet" href="https://fonts.googleapis.com/css2?family=Raleway:wght@300;400&family=Roboto+Condensed:wght@300&display=swap">
<style>
  :root {
    --backdrop: #d9dadd;
    --turquoise: #2ea5b4;
    --turquoise-side: #38b8c6;
    --turquoise-pale: #95c5cb;
    --turquoise-pale-side: #9fd0d6;
    --accent-tint: rgba(255, 255, 255, 0.22);
    --ink: #16262e;
    --ink-soft: #2f4d57;
    --ink-muted: #4c6e78;
  }
  html, body {
    margin: 0;
    width: 1200px;
    height: 1200px;
    overflow: hidden;
    background: var(--backdrop);
  }
  .canvas {
    position: relative;
    width: 1200px;
    height: 1200px;
    display: flex;
    justify-content: center;
    align-items: center;
  }
  .carton {
    display: flex;
    height: 1040px;
    box-shadow: 0 12px 30px rgba(0, 0, 0, 0.12);
  }
  .panel {
    position: relative;
    height: 100%;
    overflow: hidden;
  }
  .panel--side {
    width: 300px;
    background: linear-gradient(to bottom, var(--turquoise-side) 0 68%, var(--turquoise-pale-side) 68% 100%);
  }
  .panel--front {
    width: 520px;
    background: linear-gradient(to bottom, var(--turquoise) 0 68%, var(--turquoise-pale) 68% 100%);
  }
  .brief-copy {
    position: absolute;
    top: 150px;
    left: 34px;
    width: 220px;
    font-family: "Roboto Condensed", sans-serif;
    font-weight: 300;
    font-size: 14.5px;
    line-height: 1.5;
    color: var(--ink);
  }
  .brief-copy p { margin: 0 0 22px; }
  .accent-circle {
    position: absolute;
    top: -120px;
    right: -130px;
    width: 360px;
    height: 360px;
    border-radius: 50%;
    background: var(--accent-tint);
  }
  .brand-name {
    position: absolute;
    left: 150px;
    bottom: 335px;
    margin: 0;
    writing-mode: vertical-rl;
    transform: rotate(180deg);
    font-family: "Raleway", sans-serif;
    font-weight: 300;
    font-size: 76px;
    letter-spacing: 1px;
    color: var(--ink);
    white-space: nowrap;
  }
  .product-info {
    position: absolute;
    right: 28px;
    top: 775px;
    text-align: right;
    font-family: "Raleway", sans-serif;
    font-weight: 300;
  }
  .product-info__purity {
    display: block;
    font-size: 24px;
    font-weight: 400;
    color: var(--ink);
  }
  .product-info__name {
    display: block;
    font-size: 62px;
    line-height: 1.05;
    color: var(--ink-soft);
  }
  .product-info__type {
    display: block;
    font-size: 30px;
    color: var(--ink-muted);
  }
  .volume {
    position: absolute;
    right: 28px;
    bottom: 36px;
    font-family: "Raleway", sans-serif;
    font-weight: 300;
    font-size: 28px;
    color: var(--ink-muted);
  }
</style>
</head>
<body>
<main class="canvas">
  <section class="carton">
    <div class="panel panel--side">
      <div class="brief-copy">
        <p>We are creating a new cosmetics brand called 'Nolan Whitby' and would like you to create an amazing logo and bottle label for this brand's new 100% pure argan oil product.</p>
        <p>For the logo, we really like the logo's of Marin Calloway and Vessa. The text should be Sans Serif (without feet).</p>
        <p>For the actual bottle label, please find attached labels of one of our competitors design which really like. We really like the simplicity and elegance of the design. The only difference is that our product will be using light turqoise as the brand color. Please feel free to add your own creativity into it as well.</p>
      </div>
    </div>
    <div class="panel panel--front">
      <div class="accent-circle" aria-hidden="true"></div>
      <h1 class="brand-name">NOLAN WHITBY</h1>
      <div class="product-info">
        <span class="product-info__purity">100% pure</span>
        <span class="product-info__name">argan oil</span>
        <span class="product-info__type">moisturizing oil</span>
      </div>
      <div class="volume">1.7 Oz / 50ml</div>
    </div>
  </section>
</main>
</body>
</html>
```